Dorvelan Swimming & Athletics Center

We need Business Card for a Athletics center
The logo frome the Uploaded Files ( b card fimal)
Οn one side of card we need the logo of company the Contact and the website:
1. Address:(Limassol, Cyprus 12-14 Stavrinelou str,Ano Trimeni,P.C. 4832)

2.Phone number: (+357) 25-704263

3. Mail: info@dorvelanfit.example

3. Website: www.dorvelanfit.example

Οn the other side of the card we need to write the sport of the company:

1. Artistic Gymnastics
2. Swimming
3. Gym - Fitness
4. Programs
5. Dancing
5.Tennis

From the Uploaded Files you can get the logo.In a logo is behind the black color which can be removed from logo.

Υou can use that color you want.
.
Updates

Industry/Entity Type

Business

Font styles to use
Decorative

Colors
0555a3
ffcf3e
3176b5
0692cd
add136
f04a50
000000
cfcfcf
9d9d9d

Requirements
Should not have
• photos with faces
• photo fro the Website:www.dorvelanfit.example

```html
<!DOCTYPE html>
<html lang="en">
<head>
<meta charset="utf-8">
<title>Dorvelan Swimming &amp; Athletics Center – Business Card</title>
<link rel="stylesheet" href="https://fonts.googleapis.com/css2?family=Tinos:wght@400;700&family=Kaushan+Script&display=swap">
<style>
  :root {
    --card-white: #ffffff;
    --card-black: #000000;
    --label-grey: #cfcfcf;
    --value-gold: #ffcf3e;
    --brand-red: #8c1c17;
    --mark-ring: #0555a3;
  }
  * { margin: 0; padding: 0; box-sizing: border-box; }
  html, body {
    width: 1200px;
    height: 857px;
    overflow: hidden;
    background: var(--card-white);
  }
  .card {
    position: relative;
    width: 1200px;
    height: 857px;
    background: var(--card-black);
    overflow: hidden;
  }
  .brand-panel {
    position: absolute;
    left: 0;
    top: 0;
    width: 419px;
    height: 857px;
    background: var(--card-white);
  }
  .brand-ring {
    position: absolute;
    left: 30px;
    top: 210px;
    width: 360px;
    height: 360px;
  }
  .brand-name {
    position: absolute;
    left: 0;
    width: 419px;
    top: 560px;
    text-align: center;
    font-family: "Tinos", "Times New Roman", serif;
    font-weight: 700;
    font-size: 56px;
    letter-spacing: 1px;
    color: var(--brand-red);
  }
  .contact-label,
  .contact-value {
    position: absolute;
    white-space: nowrap;
    line-height: 1;
  }
  .contact-label {
    left: 457px;
    font-family: "Tinos", "Times New Roman", serif;
    font-weight: 400;
    font-size: 37px;
    color: var(--label-grey);
  }
  .contact-value {
    left: 726px;
    font-family: "Kaushan Script", cursive;
    font-size: 38px;
    color: var(--value-gold);
  }
  .contact-value--small { font-size: 31px; }
</style>
</head>
<body>
  <main class="card">
    <section class="brand-panel">
      <svg class="brand-ring" viewBox="0 0 360 360" aria-hidden="true">
        <circle cx="180" cy="180" r="150" fill="none" stroke="var(--mark-ring)" stroke-width="10"/>
      </svg>
      <div class="brand-name">DORVELAN</div>
    </section>

    <section class="contact-details">
      <span class="contact-label" style="top:126px">Address:</span>
      <span class="contact-value" style="top:120px">Limassol, Cyprus 12-14</span>
      <span class="contact-value" style="top:215px">Stavrinelou str,</span>
      <span class="contact-value" style="top:320px">Ano Trimeni,</span>
      <span class="contact-value" style="top:418px">P.C. 4832</span>

      <span class="contact-label" style="top:550px">Tel:</span>
      <span class="contact-value" style="top:549px">(+357) 25-704263</span>

      <span class="contact-label" style="top:626px">Email:</span>
      <span class="contact-value contact-value--small" style="top:626px">info@dorvelanfit.example</span>

      <span class="contact-label" style="top:690px">Web:</span>
      <span class="contact-value contact-value--small" style="top:690px">www.dorvelanfit.example</span>
    </section>
  </main>
</body>
</html>
```